Need webdesign for service company that provides Car hiring service and transit service

We need a web design for a company that provides airport transit services and transport services including Limo, Corporate cars, Disability transit, Family transit service. We need is a simple and professional design.

Below is site which we like and also offer the same service http://www.ridelyntrek.com.au/

Reason: Waiting for the Feedback from multiple stakeholders. Need the time to select and approve the design

Target Market(s)

Tourism, Travel

Industry/Entity Type

Airport

Number of Pages Required

3 page

Font styles to use
Decorative
Script

Requirements
Must have
• Simple and Professional, Site we like http://www.ridelyntrek.com.au/ and also need to mobile friendly
Should not have
• Shouldn't have too many images

```html
<!DOCTYPE html>
<html lang="en">
<head>
<meta charset="utf-8">
<title>GOWAVE – Private &amp; Business Transport</title>
<link href="https://fonts.googleapis.com/css2?family=Lato:wght@400;700;900&family=Sorts+Mill+Goudy&display=swap" rel="stylesheet">
<style>
:root{
  --ink:#111;
  --black:#000;
  --grey:#777274;
  --mid:#555;
  --light:#f2f2f2;
  --line:#cfcfcf;
  --white:#fff;
}
*{box-sizing:border-box;margin:0;padding:0}
html,body{width:993px;height:1200px;overflow:hidden;background:var(--white);font-family:'Lato',sans-serif;color:var(--ink)}
.page{position:relative;width:993px;height:1200px}
.topbar{position:absolute;left:0;top:0;width:100%;height:4px;background:var(--black)}
.brand{position:absolute;left:84px;top:26px;display:flex;align-items:center;gap:12px}
.brand-mark{width:44px;height:44px;border:3px solid var(--ink)}
.brand-name{font-size:32px;font-weight:900;line-height:1;color:var(--ink)}
.brand-tag{font-size:8.6px;font-weight:700;color:var(--mid);letter-spacing:.2px;margin-top:3px}
.diamond-btn{position:absolute;width:30px;height:30px;transform:rotate(45deg);border:1.6px solid var(--ink);background:var(--white)}
.diamond-btn svg{position:absolute;left:50%;top:50%;width:17px;height:17px;transform:translate(-50%,-50%) rotate(-45deg)}
.phone-number{position:absolute;left:694px;top:42px;font-size:16px;font-weight:700}
.intro{position:absolute;left:0;top:106px;width:100%;height:114px;background:linear-gradient(#eeeeee,#fafafa);text-align:center}
.intro h1{font-family:'Sorts Mill Goudy',serif;font-weight:400;font-size:30px;margin-top:28px;line-height:1;color:var(--ink)}
.intro h1 .amp{font-size:38px}
.intro .rule{width:300px;height:1px;background:var(--mid);margin:0 auto}
.intro p{font-size:16px;color:var(--mid);margin-top:2px}
.hero{position:absolute;left:0;top:220px;width:100%;height:457px;background:linear-gradient(180deg,#c9cbc8 0%,#8d9190 35%,#5d6061 70%,#0f0f0f 100%)}
.quote{position:absolute;left:636px;top:310px;width:276px;height:264px;background:var(--black)}
.quote-head{height:58px;background:var(--grey);color:var(--white);font-size:19.5px;font-weight:700;display:flex;align-items:center;justify-content:center}
.field{position:absolute;left:10px;width:256px;background:var(--white);display:flex;font-size:9.6px}
.field .ico{width:27px;border-right:1px solid #ddd;display:flex;align-items:center;justify-content:center}
.field .txt{padding-left:10px;display:flex;flex-direction:column;justify-content:center;gap:8px}
.plus{display:inline-block;width:11px;height:11px;border:1px solid #bbb;font-size:9px;line-height:9px;text-align:center;margin-right:6px}
.estimate{position:absolute;left:671px;top:552px;width:206px;height:34px;background:var(--grey);color:var(--white);font-size:16px;font-weight:700;display:flex;align-items:center;justify-content:center}
.service{position:absolute;top:760px;width:194px;height:176px;border:1px solid var(--line);text-align:center}
.service-icon{position:absolute;left:50%;top:-45px;width:64px;height:64px;margin-left:-32px;transform:rotate(45deg);border:3px solid var(--ink);background:var(--white);outline:6px solid var(--white)}
.service-icon svg{position:absolute;left:50%;top:50%;width:38px;height:38px;transform:translate(-50%,-50%) rotate(-45deg)}
.service h2{margin-top:68px;font-size:14.5px;font-weight:700;white-space:nowrap}
.service p{margin-top:10px;font-size:11.5px;line-height:17px;padding:0 10px}
.about{position:absolute;left:0;top:974px;width:100%;height:188px;background:#eeeeee;text-align:center}
.about h2{font-size:24px;font-weight:400;margin-top:30px}
.about h2 b{font-weight:900}
.about p{width:780px;margin:12px auto 0;font-size:11.2px;line-height:21.6px}
.footer{position:absolute;left:0;top:1162px;width:100%;height:38px;background:var(--black);color:var(--white)}
.footer .copy{position:absolute;left:83px;top:12px;font-size:11.6px}
.social{position:absolute;top:11px;width:16px;height:16px;transform:rotate(45deg);border:1.3px solid var(--white)}
</style>
</head>
<body>
<div class="page">
  <div class="topbar"></div>

  <header>
    <div class="brand">
      <div class="brand-mark"></div>
      <div>
        <div class="brand-name">GOWAVE</div>
        <div class="brand-tag">RIDE IN COMFORT EVERY DAY</div>
      </div>
    </div>
    <div class="diamond-btn" style="left:648px;top:38px"><svg viewBox="0 0 24 24"><path d="M6.6 10.8a15 15 0 0 0 6.6 6.6l2.2-2.2a1 1 0 0 1 1-.25 11.4 11.4 0 0 0 3.6.57 1 1 0 0 1 1 1V20a1 1 0 0 1-1 1A17 17 0 0 1 3 4a1 1 0 0 1 1-1h3.5a1 1 0 0 1 1 1c0 1.250.2 2.450.57 3.57a1 1 0 0 1-.25 1z" fill="#111"/></svg></div>
    <div class="phone-number">123 456 7890</div>
    <div class="diamond-btn" style="left:824px;top:38px"><svg viewBox="0 0 24 24"><path d="M4 6h16M4 12h16M4 18h16" stroke="#111" stroke-width="2.6"/></svg></div>
    <div class="diamond-btn" style="left:874px;top:38px"><svg viewBox="0 0 24 24"><circle cx="10" cy="10" r="6" fill="none" stroke="#111" stroke-width="2.4"/><path d="M14.5 14.5L20 20" stroke="#111" stroke-width="2.6"/></svg></div>
  </header>

  <section class="intro">
    <h1>Private <span class="amp">&amp;</span> Business</h1>
    <div class="rule"></div>
    <p>Personalised Transport Services</p>
  </section>

  <section class="hero" role="img" aria-label="Silver sedan driving along a motorway"></section>

  <form class="quote">
    <div class="quote-head">GET INSTANT QUOTE</div>
    <div class="field" style="top:88px;height:31px"><div class="ico"><svg width="10" height="10"><circle cx="5" cy="5" r="4" fill="none" stroke="#111"/></svg></div><div class="txt">Origin ( Public Location Or Exact Address )</div></div>
    <div class="field" style="top:130px;height:31px"><div class="ico"><svg width="10" height="13" viewBox="0 0 10 13"><path d="M5 0a4.5 4.5 0 0 0-4.5 4.5C.5 8 5 13 5 13s4.5-5 4.5-8.5A4.5 4.5 0 0 0 5 0z" fill="#333"/><circle cx="5" cy="4.5" r="1.6" fill="#fff"/></svg></div><div class="txt">Destination ( Public Location Or Exact Address )</div></div>
    <div class="field" style="top:173px;height:49px"><div class="ico"><svg width="10" height="10"><circle cx="5" cy="5" r="4" fill="none" stroke="#111"/></svg></div><div class="txt"><span>Show other vehicles</span><span><span class="plus">+</span>Add Stops</span></div></div>
  </form>
  <div class="estimate">ESTIMATE FARE</div>

  <section class="services">
    <article class="service" style="left:82px">
      <div class="service-icon"><svg viewBox="0 0 40 40"><path d="M4 26v-6l4-2 5-6h13l6 6 4 1v7z" fill="#222"/><path d="M14 13.5h5v4.5h-9zM21 13.5h4.5l4 4.5H21z" fill="#fff"/><circle cx="11" cy="27" r="3.5" fill="#222" stroke="#fff" stroke-width="1.5"/><circle cx="30" cy="27" r="3.5" fill="#222" stroke="#fff" stroke-width="1.5"/></svg></div>
      <h2>CORPORATE CARS</h2>
      <p>Lorem ipsum dolor sit amet conse adipiscing elit maecena commod sem neciscin...[+]</p>
    </article>
    <article class="service" style="left:293px">
      <div class="service-icon"><svg viewBox="0 0 40 40"><path d="M6 30V18l4-8h20l4 8v12h-5v-3H11v3z" fill="#222"/><path d="M11.5 12h17l2.5 5H9z" fill="#fff"/><path d="M14 20v6M17 20v6M20 20v6M23 20v6M26 20v6" stroke="#fff"/></svg></div>
      <h2>LIMO SERVICE</h2>
      <p>Lorem ipsum dolor sit amet conse adipiscing elit maecena commod sem neciscin...[+]</p>
    </article>
    <article class="service" style="left:504px">
      <div class="service-icon"><svg viewBox="0 0 40 40"><circle cx="15" cy="7" r="3" fill="#222"/><path d="M15 12v10h9l4 9" fill="none" stroke="#222" stroke-width="3"/><path d="M11 17a9 9 0 1 0 12 11" fill="none" stroke="#222" stroke-width="2.6"/></svg></div>
      <h2>DISABILITY TRANSIT</h2>
      <p>Lorem ipsum dolor sit amet conse adipiscing elit maecena commod sem neciscin...[+]</p>
    </article>
    <article class="service" style="left:716px">
      <div class="service-icon"><svg viewBox="0 0 40 40"><rect x="6" y="6" width="24" height="24" rx="4" fill="#222"/><rect x="9" y="10" width="18" height="8" fill="#fff"/><circle cx="11" cy="24" r="1.8" fill="#fff"/><circle cx="25" cy="24" r="1.8" fill="#fff"/><rect x="8" y="30" width="4" height="4" fill="#222"/><rect x="24" y="30" width="4" height="4" fill="#222"/></svg></div>
      <h2>FAMILY TRANSIT SERVICE</h2>
      <p>Lorem ipsum dolor sit amet conse adipiscing elit maecena commod sem neciscin...[+]</p>
    </article>
  </section>

  <section class="about">
    <h2>ABOUT <b>US</b></h2>
    <p>Fusce a lorem felis. Nulla quis tellus vulputate, pellentesque tortor in, dictum ligula. Ut pretium sem elit, quis luctus eros blandit sed. Mauris nec lacus elementum, vulputate orci sed, ullamcorper nulla. Etiam tempor lorem quis metus imperdiet aliquet. Vestibulum at mi risus. Sed mattis maximus tristique. Vivamus sollicitudin tellus sed velit accumsan, sed iaculis ligula dignissim. Maecenas accumsan ut dui vel commodo. Integer varius tortor at ipsum efficitur lobortis. Ut posuere in dui nec bibendum sed a lectus bibendum est iaculis dignissim.</p>
  </section>

  <footer class="footer">
    <div class="copy">Copyright © 2017 GOWAVE. All Rights Reserved.</div>
    <div class="social" style="left:835px"></div>
    <div class="social" style="left:863px"></div>
    <div class="social" style="left:891px"></div>
  </footer>
</div>
</body>
</html>
```